Homecare Design. I would like the color to be same as my business cards

Gentle Hearthkeeper & Helper Agency
I would something very light on the eyes.
Easy to read nothing complicated
I want something that demonstrate soft touch

My contact number has change cell: 203-555-0187 office: 2035550142

Target Market(s)

Elderly
people looking for someone to take care of there love ones
Target age starting at 50

Industry/Entity Type

Business

Font styles to use
Serif

Colors
3176b5
3276b5
85acd3
ceddec

Requirements
Must have

Nice to have
• I woluld like something like helping hands
Should not have
• I really don't care to see medical supplies, medication

```html
<!DOCTYPE html>
<html lang="en">
<head>
<meta charset="utf-8">
<title>Gentle Hearthkeeper &amp; Helper Agency – Postcard</title>
<link rel="stylesheet" href="https://fonts.googleapis.com/css2?family=Marcellus+SC&family=Fjalla+One&family=Oswald:wght@300;400&family=Arimo:ital,wght@0,400;1,400&display=swap">
<style>
  :root {
    --page: #ffffff;
    --band: #7b94cb;
    --band-deep: #6f88c2;
    --ribbon: #4a4f9c;
    --ink-brand: #4b4a9c;
    --ink-light: #eef1fb;
    --teal: #17999a;
    --teal-soft: #2aa3a3;
    --list-ink: #45454f;
    --panel-top: #eeeefa;
    --panel-bottom: #a6a6df;
    --photo-warm: #c9b7ae;
    --photo-cool: #d9dde6;
    --rule: #555;
  }
  * { box-sizing: border-box; margin: 0; padding: 0; }
  html, body { width: 822px; height: 1200px; overflow: hidden; background: var(--page); }
  .canvas { position: relative; width: 822px; height: 1200px; }

  /* ---------- front ---------- */
  .card-front {
    position: absolute; left: 40px; top: 40px; width: 723px; height: 548px;
    overflow: hidden; background: var(--page);
  }
  .front-photo {
    position: absolute; left: 0; top: 0; width: 723px; height: 400px;
    background: linear-gradient(100deg, var(--photo-cool) 0%, var(--photo-warm) 35%, #e9e6e6 60%, var(--photo-cool) 100%);
  }
  .front-shapes { position: absolute; left: 0; top: 0; }
  .ribbon {
    position: absolute; left: 452px; top: 285px; width: 268px; height: 74px;
    transform: rotate(7deg); transform-origin: left top;
    color: #fff; font-family: "Fjalla One", sans-serif; font-size: 19px;
    line-height: 24px; text-align: center; padding-top: 12px;
  }
  .front-name {
    position: absolute; left: 0; width: 723px; top: 390px; text-align: center;
    font-family: "Marcellus SC", serif; font-size: 36px; color: var(--ink-brand);
    letter-spacing: 0.5px;
  }
  .front-contact {
    position: absolute; font-family: "Oswald", sans-serif; font-weight: 300;
    color: var(--ink-light); display: flex; align-items: center; gap: 14px;
  }
  .front-contact.phone { font-size: 28px; top: 440px; }
  .front-contact.office { left: 112px; }
  .front-contact.cell { left: 400px; }
  .front-contact.line { font-size: 18px; top: 490px; }
  .front-contact.address { left: 82px; }
  .front-contact.web { left: 398px; }

  /* ---------- back ---------- */
  .card-back {
    position: absolute; left: 33px; top: 605px; width: 737px; height: 548px;
    background: var(--page); overflow: hidden;
  }
  .back-panel { position: absolute; left: 0; top: 0; }
  .back-name {
    position: absolute; left: 0; width: 380px; top: 12px; text-align: center;
    font-family: "Marcellus SC", serif; font-size: 17px; line-height: 25px; color: var(--ink-brand);
  }
  .back-phones {
    position: absolute; left: 0; width: 380px; top: 63px; text-align: center;
    font-family: "Oswald", sans-serif; font-size: 15px; color: #2f2f6a;
  }
  .back-web {
    position: absolute; left: 0; width: 380px; top: 91px; text-align: center;
    font-family: "Marcellus SC", serif; font-size: 12px; color: var(--ink-brand);
  }
  .back-photo {
    position: absolute; left: 21px; top: 127px; width: 157px; height: 130px;
    border: 1px solid #999;
    background: linear-gradient(135deg, #d8cfc7 0%, #bfb1a8 45%, #e6e0da 100%);
  }
  .back-intro {
    position: absolute; left: 184px; top: 133px; width: 170px;
    font-family: "Marcellus SC", serif; font-size: 12.5px; line-height: 19px; color: var(--teal);
    font-weight: 700;
  }
  .service-list {
    position: absolute; left: 28px; top: 266px; list-style: none;
    font-family: "Fjalla One", sans-serif; font-size: 14.5px; line-height: 20.5px;
    color: var(--list-ink); text-shadow: 1px 1px 1px rgba(0,0,0,0.18);
  }
  .service-list li { position: relative; padding-left: 33px; }
  .service-list li::before { content: "•"; position: absolute; left: 0; }
  .back-cta {
    position: absolute; left: 0; width: 380px; top: 490px; text-align: center;
    font-family: "Arimo", sans-serif; font-style: italic; font-size: 16px; line-height: 20px; color: var(--teal-soft);
  }
  .mail-address {
    position: absolute; left: 448px; top: 48px;
    font-family: "Arimo", sans-serif; font-size: 15px; color: #111;
  }
  .stamp-box {
    position: absolute; left: 632px; top: 197px; width: 77px; height: 93px;
    border: 1px solid var(--rule);
    font-family: "Arimo", sans-serif; font-size: 9px; line-height: 12px;
    text-align: center; padding-top: 28px; color: #222;
  }
  .label-area {
    position: absolute; left: 388px; top: 370px; width: 326px; height: 118px;
    border: 1px dotted var(--rule);
  }
</style>
</head>
<body>
<div class="canvas">

  <section class="card-front">
    <div class="front-photo" role="img" aria-label="Photo of a smiling young caregiver talking with an elderly woman over a cup of tea"></div>
    <svg class="front-shapes" width="723" height="548" viewBox="0 0 723 548" aria-hidden="true">
      <path d="M0 352 C 200 392, 470 385, 723 262 L723 548 L0 548 Z" fill="#ffffff"/>
      <path d="M0 365 C 210 405, 480 395, 723 285 L723 548 L0 548 Z" fill="var(--band)"/>
      <path d="M452 285 L720 318 L712 392 L446 358 Q 455 322 452 285 Z" fill="var(--ribbon)"/>
    </svg>
    <p class="ribbon">Compassionate and professional.<br>Our caring staff is here to help.</p>

    <h1 class="front-name">Gentle Hearthkeeper &amp; Helper Agency</h1>

    <p class="front-contact phone office">
      <svg width="26" height="28" viewBox="0 0 24 24" aria-hidden="true"><path fill="var(--ink-light)" d="M6.6 2.5c.6-.3 1.3 0 1.6.6l1.6 3.4c.3.6.1 1.2-.4 1.6L7.9 9.2c1 2.4 2.8 4.5 5.1 5.8l1.3-1.4c.4-.5 1.1-.6 1.6-.3l3.3 1.8c.6.3.8 1 .6 1.6l-.9 2.3c-.3.8-1.1 1.3-2 1.2C9.8 19.5 4.3 13.4 4.2 6.3c0-.9.5-1.7 1.3-2z"/></svg>
      <span>203-555-0142</span>
    </p>
    <p class="front-contact phone cell">
      <svg width="20" height="28" viewBox="0 0 16 24" aria-hidden="true"><rect x="2" y="1" width="12" height="22" rx="2" fill="var(--ink-light)"/><rect x="4" y="4" width="8" height="13" fill="var(--band)"/><circle cx="8" cy="20" r="1.2" fill="var(--band)"/></svg>
      <span>203-555-0187</span>
    </p>
    <p class="front-contact line address">48 Linden Ave, Milford, CT 06460</p>
    <p class="front-contact line web">gentlehearthkeeperhelper.com</p>
  </section>

  <section class="card-back">
    <svg class="back-panel" width="737" height="548" viewBox="0 0 737 548" aria-hidden="true">
      <defs>
        <linearGradient id="panelFade" x1="0" y1="0" x2="1" y2="1">
          <stop offset="0" stop-color="var(--panel-top)"/>
          <stop offset="1" stop-color="var(--panel-bottom)"/>
        </linearGradient>
      </defs>
      <path d="M0 0 L372 0 C 400 100, 398 220, 365 305 C 335 385, 322 470, 314 548 L0 548 Z" fill="url(#panelFade)" stroke="#7fb7b7" stroke-width="1"/>
    </svg>

    <h2 class="back-name">Gentle Hearthkeeper<br>&amp; Helper Agency</h2>
    <p class="back-phones">203-555-0142 or 203-555-0187</p>
    <p class="back-web">gentlehearthkeeperhelper.com</p>

    <div class="back-photo" role="img" aria-label="Photo of four cheerful seniors giving a thumbs up"></div>
    <p class="back-intro">Our home care services assist elderly clients with daily living in or out of the home, allowing them to lead lives of their choice.</p>

    <ul class="service-list">
      <li>Assistance with Daily Living</li>
      <li>Light cooking</li>
      <li>Light Housekeeping</li>
      <li>Running errands</li>
      <li>Accompaniment to Doctors visits</li>
      <li>Laundry</li>
      <li>In and out home activities</li>
      <li>Medication reminders</li>
      <li>Hours of services range from 4 hrs</li>
      <li>to live-in services</li>
    </ul>

    <p class="back-cta">Call us for a free consultation<br>and care plan!</p>

    <p class="mail-address">48 Linden Ave, Milford, CT 06460</p>
    <div class="stamp-box">PLACE<br>STAMP<br>HERE</div>
    <div class="label-area"></div>
  </section>

</div>
</body>
</html>
```